Promotional brochure for educational consulting firm

Updates

Hi Designers!

Please do a 8.5 x 11 inch tri-fold brochure as well as a 8.5 x 11 inch half-fold brochure.  I appreciate black and white versions in addition to color.  Please take a look at my company's website for a better sense of the look and feel I am going for:  www.brightlarkco.org

Thanks!

Industry/Entity Type

Consulting

Colors
3176b5
85abd2
fcfbfd

```html
<!DOCTYPE html>
<html lang="en">
<head>
<meta charset="utf-8">
<title>Brightlark Associates – Tri-fold Brochure Inside Spread</title>
<link rel="stylesheet" href="https://fonts.googleapis.com/css2?family=Questrial&family=Open+Sans:wght@700;800&display=swap">
<style>
  :root {
    --brand-blue: #3176b5;
    --soft-blue: #85abd2;
    --bubble-blue: #c6dbef;
    --paper: #fcfbfd;
    --ink: #3a3a3a;
    --stage: #1c1c1c;
  }
  * { box-sizing: border-box; margin: 0; padding: 0; }
  html, body { width: 1200px; height: 800px; overflow: hidden; background: var(--stage); }
  body { font-family: "Questrial", "Helvetica Neue", Arial, sans-serif; color: var(--ink); }

  .spread {
    position: absolute; left: 100px; top: 13px;
    width: 1000px; height: 773px;
    background: var(--paper);
    display: flex;
  }
  .panel { position: relative; width: 333.33px; height: 100%; }
  .panel + .panel { border-left: 1px solid #e6e5ea; }

  /* Left panel */
  .photo-art { position: absolute; left: 0; width: 100%; }
  .photo-pencils { top: 0; height: 240px; }
  .photo-books { bottom: 0; height: 210px; }

  .title-box {
    position: absolute; left: 26px; top: 250px; width: 285px;
    background: var(--brand-blue); color: var(--paper);
    border-radius: 4px 4px 22px 4px;
    padding: 12px 16px 12px 18px;
  }
  .title-box .company {
    font-weight: 400; font-size: 40px; line-height: 40px; letter-spacing: 0.5px; text-transform: uppercase;
  }
  .title-box .tagline { font-size: 15px; line-height: 17px; margin-top: 6px; }
  .intro {
    position: absolute; left: 26px; top: 406px; width: 290px;
    font-size: 17px; line-height: 21px;
  }

  /* Middle panel */
  .questions { position: absolute; left: 0; top: 0; }
  .bubble {
    position: absolute; left: 14px; width: 300px;
    background: var(--bubble-blue);
    border-radius: 14px;
    padding: 8px 16px 8px 24px;
    font-size: 17px; line-height: 21px; color: #4a4a4a;
  }
  .bubble::after {
    content: ""; position: absolute; left: -2px; bottom: -8px;
    border-left: 14px solid transparent; border-right: 10px solid transparent;
    border-top: 12px solid var(--bubble-blue); transform: skewX(-20deg);
  }
  .cta {
    position: absolute; left: 0; bottom: 0; width: 100%; height: 186px;
    background: var(--brand-blue); color: var(--paper);
    border-radius: 34px 0 0 0;
    padding: 56px 22px 0 26px;
  }
  .cta .ask { font-family: "Open Sans", Arial, sans-serif; font-weight: 700; font-size: 16px; line-height: 20px; }
  .cta .answer { font-family: "Open Sans", Arial, sans-serif; font-weight: 800; font-size: 25px; line-height: 32px; letter-spacing: 0.5px; }

  /* Right panel */
  .panel-founder { display: flex; flex-direction: column; padding: 22px 22px 0 26px; }
  .portrait {
    display: block; align-self: flex-end; margin-right: 4px;
    width: 140px; height: 150px; flex: none;
  }
  .founder { margin-top: 18px; }
  .founder .name { font-size: 16px; line-height: 19px; color: #222; }
  .founder .bio { font-size: 13.5px; line-height: 17px; margin-top: 4px; }
  .expertise-heading {
    margin-top: 24px;
    color: var(--brand-blue); font-weight: 400; font-size: 29px; line-height: 31px; text-transform: uppercase;
  }
  .expertise-list {
    margin-top: 18px; padding-left: 18px;
    list-style: none; font-size: 16px; line-height: 28px; color: #2c2c2c;
  }
  .expertise-list li::before {
    content: ""; display: inline-block; width: 6px; height: 6px; border-radius: 50%;
    background: #2c2c2c; margin: 0 14px 3px -20px; vertical-align: middle;
  }
</style>
</head>
<body>
<main class="spread">

  <section class="panel panel-intro">
    <svg class="photo-art photo-pencils" viewBox="0 0 333 240" role="img" aria-label="Photo of coloured pencils fanned across a table">
      <defs>
        <linearGradient id="pencilTones" x1="0" y1="0" x2="1" y2="1">
          <stop offset="0" stop-color="#c94a3c"/>
          <stop offset="0.35" stop-color="#e7a65a"/>
          <stop offset="0.65" stop-color="#7a9fcf"/>
          <stop offset="1" stop-color="#6b3f8a"/>
        </linearGradient>
      </defs>
      <polygon points="0,0 333,0 333,190 0,225" fill="url(#pencilTones)"/>
      <line x1="0" y1="232" x2="333" y2="196" stroke="#3176b5" stroke-width="2"/>
    </svg>

    <div class="title-box">
      <h1 class="company">Brightlark<br>Associates</h1>
      <p class="tagline">provides just-in-time support to schools and school leaders.</p>
    </div>

    <p class="intro">Schools along the continuum of organizational growth—from startup schools to developing or mature schools—can benefit from specialized expertise to complete a time-sensitive special project or develop strategies and processes to take their program to the next level of excellence.</p>

    <svg class="photo-art photo-books" viewBox="0 0 333 210" role="img" aria-label="Photo of library bookshelves filled with books">
      <defs>
        <linearGradient id="bookTones" x1="0" y1="0" x2="1" y2="0">
          <stop offset="0" stop-color="#3c6fa8"/>
          <stop offset="0.4" stop-color="#c9b48a"/>
          <stop offset="0.7" stop-color="#9a6b45"/>
          <stop offset="1" stop-color="#d8d2c4"/>
        </linearGradient>
      </defs>
      <line x1="0" y1="52" x2="333" y2="10" stroke="#3176b5" stroke-width="2"/>
      <polygon points="0,62 333,20 333,210 0,210" fill="url(#bookTones)"/>
    </svg>
  </section>

  <section class="panel panel-questions">
    <svg class="questions" viewBox="0 0 333 30" width="333" height="30" aria-hidden="true">
      <line x1="0" y1="28" x2="40" y2="0" stroke="#3176b5" stroke-width="2"/>
    </svg>
    <p class="bubble" style="top:22px">How do I develop a high-functioning board?</p>
    <p class="bubble" style="top:96px">What policies do start-up schools need to have on day one?</p>
    <p class="bubble" style="top:170px">Is my meal program optimizing revenue?</p>
    <p class="bubble" style="top:238px">We want to refinance our property. How do we tell our story to a lender?</p>
    <p class="bubble" style="top:334px">How can we increase parent engagement?</p>
    <p class="bubble" style="top:404px">What do we need to do to increase visibility (and enrollment)?</p>
    <p class="bubble" style="top:494px; z-index:1">My assistant principal is going out on extended leave… can I get someone to step in while he’s out?</p>
    <div class="cta">
      <p class="ask">Do these questions<br>keep you up at night?</p>
      <p class="answer">IF SO, WE CAN HELP</p>
    </div>
  </section>

  <section class="panel panel-founder">
    <svg class="portrait" viewBox="0 0 140 150" role="img" aria-label="Portrait photo of the founder">
      <defs>
        <linearGradient id="portraitTones" x1="0" y1="0" x2="0" y2="1">
          <stop offset="0" stop-color="#9aa3ad"/>
          <stop offset="1" stop-color="#4a4f55"/>
        </linearGradient>
      </defs>
      <rect width="140" height="150" rx="16" fill="url(#portraitTones)"/>
    </svg>

    <div class="founder">
      <p class="name">Marisa Lang, Ed.D.<br>Founder &amp; CEO</p>
      <p class="bio">My 10-year experience as an executive director of charter schools in the two largest school districts in California gives me a unique “education + business” perspective in addition to a network of on-call, expert associates who are ready to assist your school in a variety of key areas.</p>
    </div>

    <h2 class="expertise-heading">Our areas of<br>expertise include:</h2>
    <ul class="expertise-list">
      <li>Board Training</li>
      <li>Budget and Operations</li>
      <li>Charter Development</li>
      <li>Communications</li>
      <li>Leadership Coaching</li>
      <li>Lender Negotiations</li>
      <li>Fund Development</li>
      <li>Placement of interim administrators</li>
    </ul>
  </section>

</main>
</body>
</html>
```